Business Card

We are looking to re-create our business card. Attached is the company logo. we would like it to be back and front. for example one side with the persons information and the other side with the company logo. Be as creative as you would like but also keep in mind, we are a Health Insurance company and we need to look professional as well.
Business

```html
<!DOCTYPE html>
<html lang="en">
<head>
<meta charset="utf-8">
<title>Northvale Health Plans — Business Card</title>
<link rel="stylesheet" href="https://fonts.googleapis.com/css2?family=PT+Sans:wght@400;700&display=swap">
<style>
  :root {
    --backdrop: #b6e3d5;
    --card-white: #f4f4f4;
    --panel-dark: #2e2c2d;
    --brand-blue: #1a8fd1;
    --blue-light: #12a3de;
    --blue-deep: #0a78c9;
    --name-grey: #9c9c9c;
    --rule-grey: #8f8f8f;
    --contact-grey: #8a8a8a;
  }
  * { margin: 0; padding: 0; box-sizing: border-box; }
  html, body {
    width: 1200px;
    height: 856px;
    overflow: hidden;
  }
  body {
    background: var(--backdrop);
    font-family: "PT Sans", sans-serif;
    display: flex;
    align-items: center;
    justify-content: center;
    gap: 60px;
  }
  .card {
    position: relative;
    width: 520px;
    height: 300px;
    background: var(--card-white);
    border-radius: 26px;
    overflow: hidden;
    box-shadow: 0 6px 18px rgba(40, 80, 70, 0.18);
  }
  .card__panel {
    position: absolute;
    inset: 0;
    width: 100%;
    height: 100%;
  }
  /* Front */
  .front__name {
    position: absolute;
    left: 30px;
    top: 134px;
    font-size: 28px;
    font-weight: 700;
    line-height: 1;
    color: var(--name-grey);
  }
  .front__rule {
    position: absolute;
    left: 180px;
    top: 96px;
    width: 1px;
    height: 90px;
    background: var(--rule-grey);
  }
  .front__company {
    position: absolute;
    left: 230px;
    top: 104px;
    font-size: 25px;
    font-weight: 700;
    line-height: 1.2;
    color: var(--brand-blue);
    white-space: nowrap;
  }
  /* Back */
  .back__contact {
    position: absolute;
    left: 250px;
    right: 24px;
    top: 34px;
    text-align: center;
    font-size: 15px;
    line-height: 1.45;
    color: var(--contact-grey);
    list-style: none;
  }
</style>
</head>
<body>
  <section class="card card--front" aria-label="Card front">
    <svg class="card__panel" viewBox="0 0 520 300" preserveAspectRatio="none" aria-hidden="true">
      <polygon points="0,0 150,0 300,300 0,300" fill="var(--panel-dark)"/>
    </svg>
    <p class="front__name">Northvale</p>
    <div class="front__rule"></div>
    <h1 class="front__company">Northvale Health Plans</h1>
  </section>

  <section class="card card--back" aria-label="Card back">
    <svg class="card__panel" viewBox="0 0 520 300" preserveAspectRatio="none" aria-hidden="true">
      <defs>
        <linearGradient id="back-band" x1="0" y1="0" x2="0" y2="1">
          <stop offset="0" stop-color="var(--blue-light)"/>
          <stop offset="1" stop-color="var(--blue-deep)"/>
        </linearGradient>
      </defs>
      <polygon points="0,0 150,0 292,300 0,300" fill="url(#back-band)"/>
    </svg>
    <ul class="back__contact">
      <li>dana@northvalehealth.com</li>
      <li>000 - 1XXXXX xx</li>
      <li>000 - XXXx - XXX</li>
    </ul>
  </section>
</body>
</html>
```